Harmonizing DEIJ and OARS_A Pathway to Inclusive Excellence

We are developing a PowerPoint presentation titled 'Harmonizing DEIJ and OARS: A Pathway to Inclusive Hospitality'. This presentation aims to showcase the synergistic approach between a regional grocery store and a DEIJ consulting firm, focusing on integrating the OARS method with Cultural Competence to foster an inclusive, hospitable environment for associates and guests. The design should be professional, accessible, and engaging, facilitating the learning and application of DEIJ and OARS principles within the grocery retail and service sectors.
Updates

I started with no days??????

I have updated information on OARS. It may be helpful. I have also updated two slide on DEIJ Change Management that need to be incorporated into the presentation.

Target Market(s)

The primary audience includes grocery store management and staff, DEIJ professionals, and individuals responsible for implementing and promoting inclusivity within retail and customer service environments. The design should appeal to a broad range of professionals interested in enhancing workplace culture and customer experience through DEIJ initiatives.

Industry/Entity Type

Retail, specifically grocery stores, and DEIJ Consulting

Font styles to use
Other font styles liked:
• Headers: Calibri Light, Body: Poppins

Colors

Designer to choose colors to be used in the design.

Requirements
Must have
• Branding: Integrate both the regional grocery store's and the DEIJ consulting firm's branding elements, ensuring a harmonious presentation style that represents the collaboration effectively. I have upload the DEIJ Consulting firm Brand Sheet, The main color for the consulting firm is #29265F. The main color for the Grocery store is #4FA130. Content Layout: Design a clear, intuitive layout that guides the viewer through the concepts of DEIJ and OARS, their integration, and practical application in retail settings. Image Use: Employ high-resolution, professional images that reflect diversity, inclusion, and the grocery retail context, supporting the content and engaging the target audience. Accessibility: Ensure the presentation is accessible, with clear font sizes and styles for readability, following ADA compliance guidelines. Interactive Elements: Incorporate sections for audience interaction, such as reflection questions, scenario-based discussions, and action planning, to foster active participation and engagement. Case Studies and Success Stories: Include slides dedicated to real-world applications, showcasing successful DEIJ initiatives within the grocery sector and lessons learned.
Nice to have
• Engagement Features: Options for live polling or feedback during the presentation to gauge understanding and collect real-time insights from participants. QR Codes: Slides for embedded QR codes linking to additional DEIJ resources or training modules for further exploration post-session.
Should not have
• Informal Graphics: Avoid cartoons or overly casual graphics that could undermine the professional and educational objectives of the presentation. Overcrowding: Maintain a balance between content, visuals, and white space to ensure the presentation is engaging without overwhelming the audience.

```html
<!DOCTYPE html>
<html lang="en">
<head>
<meta charset="utf-8">
<title>DEIJ and OARS: A Pathway to Inclusive Hospitality – Slide Overview</title>
<link href="https://fonts.googleapis.com/css2?family=Poppins:wght@300;400;500&display=swap" rel="stylesheet">
<style>
:root{
  --navy:#29265F;
  --gold:#B8924A;
  --ink:#2b2a45;
  --muted:#7d7b95;
  --line:#e6e5ef;
  --paper:#ffffff;
  --soft:#f3f3f6;
}
*{box-sizing:border-box;margin:0;padding:0}
html,body{width:1200px;height:2646px;overflow:hidden;background:var(--paper)}
body{font-family:'Poppins',sans-serif;color:var(--ink);position:relative}
.slide{position:absolute;width:470px;height:263px;background:var(--paper);overflow:hidden;box-shadow:0 26px 34px -8px rgba(41,38,95,.14)}
.slide.dark{background:var(--navy);color:#fff}
.col-l{left:101px}.col-r{left:622px}
.abs{position:absolute}
.brand{position:absolute;left:8px;top:6px;display:flex;align-items:center;gap:3px;font-size:5px;font-weight:500;line-height:1.05;color:var(--navy);width:44px}
.brand i{width:9px;height:9px;border-radius:50%;background:var(--gold);flex:none}
.dark .brand{color:#fff}
.meta{position:absolute;right:30px;top:9px;font-size:4.5px;color:#b3b2c2;letter-spacing:.2px}
.dark .meta{color:#fff}
.meta b{font-weight:400;margin-left:10px}
.accent{position:absolute;display:flex;align-items:center;gap:2px}
.accent span{height:2px;background:var(--navy);width:18px}
.accent em{height:2px;width:3px;background:var(--gold)}
.accent u{height:2px;width:6px;background:var(--gold);text-decoration:none}
.dark .accent span{background:#fff}
.title{position:absolute;font-weight:300;font-size:15px;line-height:25.5px;text-transform:uppercase;color:var(--ink);letter-spacing:.1px;white-space:nowrap}
.title.plain{text-transform:none}
.dark .title{color:#fff}
.photo{position:absolute;background:linear-gradient(135deg,#5b5a6e,#a9a4a0 55%,#3e3b4f)}
.card{position:absolute;background:#fff;box-shadow:0 6px 12px rgba(41,38,95,.13);display:flex;flex-direction:column;align-items:center;justify-content:center;text-align:center;font-size:6.4px;line-height:1.55;color:var(--ink);padding:6px}
.card.navy{background:var(--navy);color:#fff}
.card.gold{background:var(--gold);color:#fff}
.card svg{width:14px;height:14px;margin-bottom:7px;stroke:var(--navy);fill:none;stroke-width:1.2}
.card.navy svg,.card.gold svg{stroke:#fff}
.pill{position:absolute;background:var(--navy);color:#fff;border-radius:10px;font-size:6.6px;display:flex;align-items:center;padding-left:12px;box-shadow:0 4px 8px rgba(41,38,95,.2);white-space:nowrap}
.bullets{position:absolute;list-style:none;font-size:6.6px;color:var(--ink)}
.bullets li{position:relative;padding-left:10px}
.bullets li::before{content:"";position:absolute;left:1px;top:4px;width:2.5px;height:2.5px;border-radius:50%;background:var(--navy)}
.row-card{position:absolute;background:#fff;box-shadow:0 5px 10px rgba(41,38,95,.12);display:flex;align-items:center;gap:12px;padding-left:10px;font-size:6.5px;line-height:1.5}
.row-card svg{width:11px;height:11px;stroke:var(--navy);fill:none;stroke-width:1.2;flex:none}
.row-card.navy{background:var(--navy);color:#fff;align-items:flex-start;padding-top:9px}
.row-card.navy svg{stroke:#fff}
.sub{font-size:5px;list-style:none;margin-top:4px;line-height:1.8}
.sub li::before{content:"• ";color:var(--gold)}
.gold-text{color:var(--gold)}
.small{font-size:6.6px;line-height:1.5;white-space:nowrap}
</style>
</head>
<body>

<!-- 1 Title -->
<section class="slide col-l" style="top:88px">
  <div class="brand" style="left:26px;top:32px;width:70px;font-size:7px;gap:5px"><i style="width:16px;height:16px"></i>Meridian Bridge Group</div>
  <h1 class="title plain" style="left:22px;top:84px;font-size:16px;line-height:25px">DEIJ and OARS: A Pathway<br>to Inclusive Hospitality</h1>
  <p class="abs" style="left:22px;top:140px;font-size:6.5px;line-height:1.55;color:var(--ink)">Operations Group Presentation<br>March 19, 2024</p>
  <div class="pill" style="left:20px;top:176px;width:74px;height:18px;color:var(--gold);font-size:7px">Dana Ellis</div>
  <p class="abs" style="left:34px;top:226px;font-size:4.5px;color:#b3b2c2">www.meridianbridge.com</p>
</section>

<!-- 2 Journey -->
<section class="slide col-r" style="top:88px">
  <div class="brand">Meridian Bridge Group</div>
  <div class="meta">www.meridianbridge.com<b>2</b></div>
  <div class="accent" style="left:22px;top:32px"><span></span><em></em><u></u></div>
  <h2 class="title" style="left:22px;top:38px">Today’s Journey</h2>
  <ul class="bullets" style="left:20px;top:85px">
    <li>Grasp DEIJ and OARS concepts with a hospitality lens.</li>
  </ul>
  <div class="pill" style="left:12px;top:101px;width:244px;height:26px;font-size:6.6px">•&nbsp;&nbsp;Integrate cultural competence into hospitality practices.</div>
  <ul class="bullets" style="left:20px;top:139px;line-height:1"><li style="margin-bottom:16px">Practice inclusive interactions to enhance guest experiences.</li><li style="margin-bottom:21px">Reflect on and grow hospitality skills through DEIJ and OARS.</li><li>Implement learnings to nurture guests’ quality of life.</li></ul>
  <div class="photo" role="img" aria-label="Photo of a diverse team in a meeting room, a smiling colleague in front" style="left:275px;top:77px;width:186px;height:135px"></div>
</section>

<!-- 3 Embracing -->
<section class="slide col-l" style="top:403px">
  <div class="brand">Meridian Bridge Group</div>
  <div class="meta">www.meridianbridge.com<b>3</b></div>
  <div class="accent" style="left:22px;top:32px"><span></span><em></em><u></u></div>
  <h2 class="title" style="left:22px;top:38px">Embracing OARS &amp;<br>DEIJ in Our Journey</h2>
  <div class="photo" role="img" aria-label="Photo of a diverse group of colleagues laughing together" style="left:214px;top:18px;width:256px;height:112px;background:linear-gradient(120deg,#c9c6c0,#6a5a4c 45%,#c79a3e 75%,#8f8a86)"></div>
  <div class="card" style="left:36px;top:107px;width:88px;height:70px"><svg viewBox="0 0 16 16"><rect x="3" y="2" width="10" height="12"/><path d="M5 6h6M5 9h6"/></svg>OARS Framework<br>Overview</div>
  <div class="card" style="left:138px;top:107px;width:86px;height:70px"><svg viewBox="0 0 16 16"><path d="M2 3h12l-5 6v5l-2-1V9z"/></svg>Merging OARS &amp;<br>DEIJ</div>
  <div class="abs" style="left:234px;top:170px;width:92px;height:46px;background:#fff;box-shadow:0 6px 12px rgba(41,38,95,.13);font-size:5.2px;line-height:1.9;padding:12px 0 0 6px;display:grid;grid-template-columns:1fr 1fr">
    <span>• Diversity</span><span>• Inclusion</span><span>• Equity</span><span>• Justice</span></div>
  <div class="card navy" style="left:234px;top:104px;width:92px;height:74px"><svg viewBox="0 0 16 16"><path d="M8 2l6 12H2z"/></svg>DEIJ Pillars<br>Explained:</div>
  <div class="card" style="left:336px;top:107px;width:90px;height:70px"><svg viewBox="0 0 16 16"><rect x="3" y="2" width="10" height="12"/><path d="M5 5h6M5 8h6M5 11h4"/></svg>DEIJ’s Role in<br>Culture</div>
</section>

<!-- 4 MI intro -->
<section class="slide col-r" style="top:403px">
  <div class="brand">Meridian Bridge Group</div>
  <div class="meta">www.meridianbridge.com<b>4</b></div>
  <div class="accent" style="left:22px;top:32px"><span></span><em></em><u></u></div>
  <h2 class="title" style="left:22px;top:38px;font-size:14.5px">Introduction to<br>Motivational Interviewing</h2>
  <div class="photo" role="img" aria-label="Photo of two women talking in a bright office, one holding a tablet" style="left:20px;top:105px;width:218px;height:123px;background:linear-gradient(120deg,#8a5a3e,#d8cfc6 50%,#3d3b3f)"></div>
  <div class="abs" style="left:398px;top:26px;width:62px;height:194px;background:var(--gold)"></div>
  <div class="row-card" style="left:266px;top:36px;width:162px;height:42px"><svg viewBox="0 0 16 16"><circle cx="8" cy="8" r="5"/><path d="M8 5v3l2 2"/></svg>Definition of Motivational<br>Interviewing</div>
  <div class="row-card" style="left:266px;top:86px;width:162px;height:42px"><svg viewBox="0 0 16 16"><path d="M3 14V3h8l-2 3 2 3H3"/></svg>Importance of MI in facilitating<br>behavior change</div>
  <div class="row-card navy" style="left:266px;top:136px;width:162px;height:73px"><svg viewBox="0 0 16 16"><path d="M8 2l6 12H2z"/></svg><div>Key principles of MI:<ul class="sub gold-text"><li>Collaboration</li><li>Evocation</li><li>Autonomy</li><li>Acceptance</li></ul></div></div>
</section>

<!-- 5 OARS overview -->
<section class="slide col-l" style="top:718px">
  <div class="brand">Meridian Bridge Group</div>
  <div class="meta">www.meridianbridge.com<b>5</b></div>
  <div class="accent" style="left:22px;top:32px"><span></span><em></em><u></u></div>
  <h2 class="title" style="left:22px;top:38px">Overview of OARS<br>Techniques</h2>
  <div class="card navy" style="left:22px;top:100px;width:130px;height:108px"><svg viewBox="0 0 16 16"><rect x="2" y="3" width="12" height="8"/><path d="M8 11v3M5 14h6"/></svg>Explanation of OARS acronym: Open-ended questions, Affirmations, Reflective listening, and Summarizing</div>
  <div class="card" style="left:168px;top:100px;width:126px;height:108px"><svg viewBox="0 0 16 16"><rect x="3" y="5" width="10" height="8"/><path d="M6 5V3h4v2"/></svg>Brief discussion on the purpose and impact of each OARS component</div>
  <div class="card" style="left:312px;top:100px;width:126px;height:108px"><svg viewBox="0 0 16 16"><circle cx="8" cy="4" r="2"/><circle cx="4" cy="11" r="2"/><circle cx="12" cy="11" r="2"/></svg>Emphasize the non-confrontational and client-centered nature of OARS.</div>
</section>

<!-- 6 Essential techniques -->
<section class="slide col-r" style="top:718px">
  <div class="brand">Meridian Bridge Group</div>
  <div class="meta">www.meridianbridge.com<b>6</b></div>
  <div class="accent" style="left:24px;top:60px"><span></span><em></em><u></u></div>
  <h2 class="title" style="left:22px;top:66px">Essential<br>Communication<br>Techniques in<br>Motivational<br>Interviewing (MI)</h2>
  <p class="abs small" style="left:240px;top:60px"><b style="font-weight:500;margin-right:10px">01</b>Open-Ended Questions – Exploring Deeply</p>
  <div class="pill" style="left:232px;top:90px;width:210px;height:24px"><b style="font-weight:500;margin-right:14px">02</b>Affirmations – Recognizing Strengths</div>
  <p class="abs small" style="left:240px;top:143px"><b style="font-weight:500;margin-right:10px">03</b>Reflective Listening – Understanding Emotions</p>
  <p class="abs small" style="left:240px;top:178px"><b style="font-weight:500;margin-right:10px">04</b>Summarizing – Bringing it All Together</p>
</section>

<!-- 7 Discussion -->
<section class="slide col-l dark" style="top:1025px">
  <div class="brand">Meridian Bridge Group</div>
  <div class="meta">www.meridianbridge.com<b>7</b></div>
  <div class="accent" style="left:22px;top:113px"><span></span><em></em><u></u></div>
  <h2 class="title plain" style="left:22px;top:119px;font-size:16px">Discussion</h2>
</section>

<!-- 8 Break -->
<section class="slide col-r dark" style="top:1025px">
  <div class="brand">Meridian Bridge Group</div>
  <div class="meta">www.meridianbridge.com<b>8</b></div>
  <div class="accent" style="left:22px;top:113px"><span></span><em></em><u></u></div>
  <h2 class="title plain" style="left:22px;top:119px;font-size:16px">Break</h2>
</section>

<!-- 9 Break with photo -->
<section class="slide col-l" style="top:1340px">
  <div class="brand">Meridian Bridge Group</div>
  <div class="meta">www.meridianbridge.com<b>9</b></div>
  <div class="photo" role="img" aria-label="Photo of colleagues working together around a laptop, with a navy overlay" style="left:38px;top:78px;width:384px;height:185px;border-radius:14px 14px 0 0;background:linear-gradient(120deg,#5d5a8e,#3a376f 50%,#4d4a80)"></div>
  <div class="accent" style="left:46px;top:157px"><span style="background:#fff"></span><em></em><u></u></div>
  <h2 class="title plain" style="left:46px;top:163px;color:#fff;font-size:16px">Break</h2>
</section>

<!-- 10 Cultivating -->
<section class="slide col-r" style="top:1340px">
  <div class="brand">Meridian Bridge Group</div>
  <div class="meta">www.meridianbridge.com<b>10</b></div>
  <div class="accent" style="left:22px;top:32px"><span></span><em></em><u></u></div>
  <h2 class="title" style="left:22px;top:38px">DEIJ and OARS in<br>Cultivating Inclusive<br>Hospitality</h2>
  <div class="photo" role="img" aria-label="Photo of three colleagues seated together in conversation" style="left:0;top:123px;width:192px;height:140px;background:linear-gradient(120deg,#ddd8d0,#3b3a44 45%,#a49c92)"></div>
  <div class="row-card" style="left:262px;top:40px;width:172px;height:28px"><svg viewBox="0 0 16 16"><circle cx="8" cy="4" r="2"/><circle cx="4" cy="11" r="2"/><circle cx="12" cy="11" r="2"/></svg>DEIJ in Hospitality</div>
  <div class="row-card" style="left:262px;top:79px;width:172px;height:28px"><svg viewBox="0 0 16 16"><path d="M2 14V2M2 14h12M4 10l3-3 3 2 4-5"/></svg>OARS for Guest Communication</div>
  <div class="row-card" style="left:262px;top:118px;width:172px;height:28px"><svg viewBox="0 0 16 16"><rect x="3" y="2" width="10" height="12"/><path d="M5 6h6M5 9h6"/></svg>Traits for Cultural Competence</div>
  <div class="row-card navy" style="left:262px;top:152px;width:172px;height:56px"><svg viewBox="0 0 16 16"><path d="M4 2h8v4a4 4 0 0 1-8 0zM8 10v4M5 14h6"/></svg><div>DEIJ &amp; OARS Integration<ul class="sub" style="font-size:4.8px"><li>Gluten-Free Guest Engagement</li><li>Cultural Product Range</li></ul></div></div>
</section>

<!-- 11 Stages -->
<section class="slide col-l" style="top:1655px">
  <div class="brand">Meridian Bridge Group</div>
  <div class="meta">www.meridianbridge.com<b>11</b></div>
  <div class="accent" style="left:22px;top:32px"><span></span><em></em><u></u></div>
  <h2 class="title" style="left:22px;top:38px">Integrating DEIJ &amp; OARS -<br>Transformative Stages in Practice</h2>
  <div class="pill" style="left:14px;top:94px;width:160px;height:18px">Transformative Stages Overview:</div>
  <div class="abs" style="left:21px;top:112px;width:1px;height:106px;background:var(--line)"></div>
  <div class="card" style="left:24px;top:122px;width:76px;height:70px;font-size:5.6px"><svg viewBox="0 0 16 16"><circle cx="8" cy="8" r="5"/><circle cx="8" cy="8" r="2"/></svg>Awareness via Open Questions</div>
  <div class="card" style="left:104px;top:122px;width:76px;height:70px;font-size:5.6px"><svg viewBox="0 0 16 16"><circle cx="8" cy="8" r="5"/><path d="M8 8l5-5"/></svg>Desire through Affirmation</div>
  <div class="card" style="left:184px;top:122px;width:76px;height:70px;font-size:5.6px"><svg viewBox="0 0 16 16"><path d="M8 2a4 4 0 0 1 2 7.5V12H6V9.5A4 4 0 0 1 8 2zM6 14h4"/></svg>Knowledge against Minimization</div>
  <div class="card navy" style="left:264px;top:119px;width:78px;height:74px;font-size:5.6px"><svg viewBox="0 0 16 16"><rect x="3" y="3" width="10" height="10"/><circle cx="8" cy="8" r="2"/></svg>Ability through Acceptance</div>
  <div class="card" style="left:346px;top:122px;width:76px;height:70px;font-size:5.6px"><svg viewBox="0 0 16 16"><rect x="2" y="3" width="12" height="8"/><path d="M4 9l3-3 2 2 3-3"/></svg>Reinforcement for Adaptation</div>
  <div class="pill" style="left:14px;top:209px;width:134px;height:18px">Discussion</div>
</section>

<!-- 12 Experiential learning -->
<section class="slide col-r" style="top:1655px">
  <div class="brand">Meridian Bridge Group</div>
  <div class="meta">www.meridianbridge.com<b>12</b></div>
  <div class="accent" style="left:22px;top:32px"><span></span><em></em><u></u></div>
  <h2 class="title" style="left:22px;top:38px">Experiential Learning with DEIJ &amp; OARS</h2>
  <p class="abs gold-text" style="left:24px;top:65px;font-size:6.3px">Activity Overview</p>
  <div class="abs" style="left:20px;top:95px;width:207px;height:135px;background:var(--soft)"></div>
  <div class="pill" style="left:18px;top:83px;width:208px;height:20px;padding-left:6px"><b style="font-weight:500;margin-right:14px">01</b>Instructions for Groups:</div>
  <div class="abs" style="left:230px;top:93px;width:30px;border-top:1px dashed var(--gold)"></div>
  <div class="pill" style="left:262px;top:83px;width:175px;height:20px;padding-left:6px"><b style="font-weight:500;margin-right:14px">02</b>Reflection and Sharing</div>
  <ul class="bullets" style="left:30px;top:110px;width:190px;font-size:5.5px;line-height:1.6;color:var(--muted)">
    <li style="margin-bottom:4px">Select a scenario or experience to discuss that involves DEIJ and hospitality.</li>
    <li style="margin-bottom:4px">Assign roles (speaker, listener, observer) within your group.</li>
    <li style="margin-bottom:4px">Engage in the scenario exercise, with the listener applying OARS techniques.</li>
    <li style="margin-bottom:4px">After the exercise, the observer shares feedback, and the group reflects on integrating DEIJ principles.</li>
    <li>Discuss how these principles can enhance hospitality and inclusivity in your workplace.</li>
  </ul>
</section>

<!-- 13 Scenarios -->
<section class="slide col-l" style="top:1970px">
  <div class="brand">Meridian Bridge Group</div>
  <div class="meta">www.meridianbridge.com<b>13</b></div>
  <div class="accent" style="left:22px;top:32px"><span></span><em></em><u></u></div>
  <h2 class="title plain" style="left:22px;top:38px;font-size:16px">Scenarios</h2>
  <div class="card" style="left:22px;top:80px;width:130px;height:128px;align-items:flex-start;justify-content:flex-start;text-align:left;padding:12px 14px;font-size:5.5px;color:var(--muted)">
    <div style="display:flex;gap:12px;color:var(--ink);font-size:6.3px;margin-bottom:16px"><svg viewBox="0 0 16 16" style="margin:0"><circle cx="4" cy="4" r="2"/><path d="M6 4h8M2 12h8"/><circle cx="12" cy="12" r="2"/></svg>Diverse Dietary<br>Needs</div>
    A guest at a store inquires about vegan dining options, expressing disappointment at the limited choices available during their last visit.</div>
  <div class="card navy" style="left:166px;top:76px;width:130px;height:134px;align-items:flex-start;justify-content:flex-start;text-align:left;padding:16px 14px;font-size:5.5px">
    <div style="display:flex;gap:12px;font-size:6.3px;margin-bottom:16px"><svg viewBox="0 0 16 16" style="margin:0"><rect x="3" y="2" width="10" height="12"/><path d="M5 6h6M5 9h6"/></svg>Language Barrier<br>in Service</div>
    A guest at a store inquires about vegan dining options, expressing disappointment at the limited choices available during their last visit.</div>
  <div class="card" style="left:310px;top:80px;width:130px;height:128px;align-items:flex-start;justify-content:flex-start;text-align:left;padding:12px 14px;font-size:5.5px;color:var(--muted)">
    <div style="display:flex;gap:12px;color:var(--ink);font-size:6.3px;margin-bottom:16px"><svg viewBox="0 0 16 16" style="margin:0"><circle cx="8" cy="4" r="2"/><circle cx="4" cy="11" r="2"/><circle cx="12" cy="11" r="2"/></svg>Cultural Sensitivity<br>During a Celebration</div>
    A couple has specific requests for their wedding ceremony that staff find unusual or difficult to understand.</div>
</section>

<!-- 14 Takeaways -->
<section class="slide col-r" style="top:1970px">
  <div class="brand">Meridian Bridge Group</div>
  <div class="meta">www.meridianbridge.com<b>14</b></div>
  <div class="accent" style="left:22px;top:32px"><span></span><em></em><u></u></div>
  <h2 class="title" style="left:22px;top:38px">Key Takeaways</h2>
  <div class="card gold" style="left:24px;top:82px;width:128px;height:110px"><svg viewBox="0 0 16 16"><path d="M2 14h12M4 14V9M7 14V7M10 14V8M13 14V4M3 7l4-3 3 2 3-3"/></svg>Insights on integrating DEIJ and OARS for enhanced hospitality.</div>
  <div class="card" style="left:168px;top:82px;width:128px;height:110px"><svg viewBox="0 0 16 16"><rect x="3" y="2" width="10" height="12"/><path d="M5 5h6M5 8h6M5 11h6"/></svg>The importance of cultural competence in nourishing guests’ quality of life.</div>
  <div class="card" style="left:312px;top:82px;width:128px;height:110px"><svg viewBox="0 0 16 16"><rect x="2" y="3" width="12" height="8"/><path d="M5 6h6M5 8h4M8 11v3"/></svg>Commitment to cultivating curiosity, open-mindedness, and a non-anxious presence.</div>
</section>

<!-- 15 Commitment -->
<section class="slide col-l" style="top:2285px">
  <div class="brand">Meridian Bridge Group</div>
  <div class="meta">www.meridianbridge.com<b>15</b></div>
  <div class="accent" style="left:22px;top:32px"><span></span><em></em><u></u></div>
  <h2 class="title" style="left:22px;top:38px">Commitment to Growth<br>and Closing Resources</h2>
  <div class="card" style="left:40px;top:110px;width:78px;height:72px"><svg viewBox="0 0 16 16"><rect x="3" y="3" width="10" height="11"/><path d="M5 11l2-2 2 1 2-3"/></svg>Recap</div>
  <div class="card navy" style="left:130px;top:106px;width:90px;height:78px"><svg viewBox="0 0 16 16"><path d="M2 3h12l-5 6v5l-2-1V9z"/></svg>Resources</div>
  <div class="card" style="left:236px;top:110px;width:88px;height:72px"><svg viewBox="0 0 16 16"><rect x="2" y="3" width="12" height="8"/><path d="M5 6h6M8 11v3"/></svg>Action Planning</div>
  <div class="card" style="left:340px;top:110px;width:88px;height:72px"><svg viewBox="0 0 16 16"><circle cx="8" cy="8" r="5"/><circle cx="8" cy="8" r="2"/><path d="M8 8l5-5"/></svg>Commitment</div>
</section>

<!-- 16 Thank you -->
<section class="slide col-r dark" style="top:2285px">
  <div class="brand">Meridian Bridge Group</div>
  <div class="meta">www.meridianbridge.com<b>16</b></div>
  <div class="accent" style="left:26px;top:96px"><span></span><em></em><u></u></div>
  <h2 class="title plain" style="left:26px;top:102px;font-size:17px">Thank You</h2>
  <p class="abs" style="left:28px;top:140px;font-size:6.5px;font-weight:500">Dana Ellis</p>
  <p class="abs" style="left:34px;top:150px;font-size:4.8px">Executive Director, Meridian Bridge Group</p>
  <p class="abs" style="left:28px;top:164px;font-size:6.5px;font-weight:500">Contact us:</p>
  <p class="abs" style="left:28px;top:174px;font-size:4.8px;line-height:1.9">• dana@meridianbridge.com<br>• +1 555 010 2040</p>
</section>

</body>
</html>
```